International travel site frontpage redesign

We sell tours to Scandinavia through our website www.velmora-journeys.com. The website has become a bit old fashioned and we are in the process of making the website responsive. As you can see from the attached pictures the website will be wider with the responsive design, and our current design does not fit anymore.

Here is what we are looking for:
- A website that reflects a trustworthy and quality oriented company.
- Making the website more modern looking, but still recognisable (we want to keep the colours).
- keeping in mind that the age group of our customers are from 20-80 years old (most in their 60s).
- We want to remove the popular tours part and are instead looking to replace this with picture boxes the following subjects Scandinavia Specialist, Special Offers, Contact, Norway (or Norway Tours), Sweden (or Sweden Tours), Iceland (or Iceland Tours), Combination Tours. Possibly also Lapland, Winter, Northern Lights, Fjords and Capitals. Some of these categories can be smaller or perhaps half boxes; i.e. Winter and Northern lights in one. If we end up with four boxes per line perhaps we could add a social media box next to the three first ones.
- The above means that the left hand meny with Norway Tours, Sweden Tours etc will be redundant.
- we will add another line to the search Box (on the top): Destinations
- The top menu will have the same categories, but we need to add languages as the website will be in English and German.
- The footer must be changed
- We can take away the box to the right where it says "your window to booking the best of our world"

Reason: One of the decission makers had to go away on business last minute.

Target Market(s)

Travelling to Scandinavia is not low cost, so the website needs to appeal to those that can afford to travel to our destination.
The age group of our customers are from 20-80 years old (most in their 60s).

Industry/Entity Type

Travel

Number of Pages Required

1 page

Requirements
Should not have
• Flashy or cheap looking special offers...

```html
<!DOCTYPE html>
<html lang="en">
<head>
<meta charset="utf-8">
<title>Velmora Journeys – Tours to Scandinavia</title>
<link rel="stylesheet" href="https://fonts.googleapis.com/css2?family=Ubuntu:wght@400;500&family=Open+Sans:wght@400;600&display=swap">
<style>
:root{
  --red:#a50d12;
  --navy:#1f2a3f;
  --navy-deep:#19223a;
  --ink:#333a45;
  --muted:#8a8f97;
  --page:#f1f1f1;
  --white:#fff;
  --sky:#1b8fe0;
  --social:#3b5897;
}
*{box-sizing:border-box;margin:0;padding:0}
html,body{width:686px;height:1200px;overflow:hidden}
body{position:relative;background:var(--page);font-family:"Open Sans",sans-serif;color:var(--ink)}
.abs{position:absolute}
ul{list-style:none}

/* header */
.site-header{left:0;top:0;width:686px;height:54px;background:var(--white);border-bottom:1px solid var(--red)}
.brand{left:30px;top:21px;font-family:"Ubuntu",sans-serif;font-size:13px;letter-spacing:.6px;color:#4a5260;text-transform:uppercase}
.main-nav{right:72px;top:25px;display:flex;gap:15px;font-family:"Ubuntu",sans-serif;font-size:7px;text-transform:uppercase;color:#9aa0a8}
.main-nav .active{color:var(--navy);font-weight:500}
.lang{right:29px;top:25px;font-family:"Ubuntu",sans-serif;font-size:7px;color:#ccc}
.lang b{color:var(--navy);font-weight:500}
.lang i{font-style:normal;color:var(--red);margin:0 2px}

/* hero */
.hero{left:30px;top:66px;width:627px;height:215px;background:linear-gradient(100deg,#2c4e86 0%,#3562a1 35%,#2f5996 55%,#3d6a5a 78%,#55733e 100%)}
.search-panel{left:0;top:0;width:172px;height:215px;background:rgba(24,34,58,.82);padding:16px 16px 0}
.field{height:19px;background:var(--white);border-radius:2px;margin-bottom:12px;font-size:6.5px;color:#777;padding:6px 6px;position:relative}
.field.select::after{content:"";position:absolute;right:7px;top:8px;border:3px solid transparent;border-top-color:#bbb}
.field.text{color:#bbb}
.field.text svg{position:absolute;right:5px;top:4px}
.search-btn{height:26px;background:var(--red);color:var(--white);font-size:7px;font-weight:600;text-align:center;line-height:26px;border-radius:2px;margin-top:1px}
.hero-copy{left:215px;top:38px;width:245px;color:var(--white)}
.hero-copy h1{font-family:"Ubuntu",sans-serif;font-weight:400;font-size:18px;margin-bottom:8px}
.hero-copy p{font-size:8.6px;line-height:14px}
.read-more{display:inline-block;margin-top:15px;border:1px solid var(--white);border-radius:2px;font-size:6.5px;padding:5px 15px;text-transform:uppercase}
.dots{left:295px;top:193px;display:flex;gap:5px}
.dots span{width:8px;height:8px;border-radius:50%;border:1px solid var(--white)}
.dots span:first-child{background:var(--red);border-color:var(--red)}

/* category tiles */
.slider-arrow{top:340px}
.tile{top:297px;width:145px;height:101px}
.tile .label{position:absolute;left:0;top:0;width:100%;height:28px;background:rgba(25,34,58,.55);color:var(--white);font-family:"Ubuntu",sans-serif;font-size:10px;padding:8px 0 0 19px}
.tile .label::before{content:"";position:absolute;left:8px;top:11px;width:4px;height:4px;border-top:1.5px solid var(--red);border-right:1.5px solid var(--red);transform:rotate(45deg)}

/* features */
.features{left:0;top:431px;width:686px;height:131px;background:var(--white)}
.feature{width:150px}
.feature .ico{position:absolute;left:0;top:0;width:27px;height:27px;background:var(--navy)}
.feature .ico.red{background:var(--red)}
.feature .ico.social{background:var(--social)}
.feature .txt{position:absolute;left:37px;top:-2px;font-family:"Ubuntu",sans-serif}
.feature small{display:block;font-size:10px;color:var(--navy)}
.feature strong{display:block;font-weight:500;font-size:17px;color:var(--red);line-height:18px;white-space:nowrap}
.feature strong em{font-style:normal;font-size:9px}
.feature .social-name{color:var(--social)}
.feature p{font-family:"Open Sans",sans-serif;font-size:6.3px;line-height:9.7px;color:#555;margin-top:3px;width:100px}

/* offers */
.tabs{left:30px;top:604px;width:627px;height:30px;border-bottom:1.5px solid var(--red);display:flex;font-family:"Ubuntu",sans-serif;font-size:10px;font-weight:500;color:var(--white)}
.tabs span{padding:9px 9px 0;background:var(--navy)}
.tabs span.on{background:var(--red);width:85px}
.offer{top:651px;width:198px;height:166px;background:var(--white);border:1px solid #e2e2e2}
.offer .photo{height:112px}
.offer .badge{position:absolute;right:-4px;top:-6px;width:42px;height:42px;border-radius:50%;background:var(--sky);color:var(--white);font-family:"Ubuntu",sans-serif;font-weight:500;font-size:9px;text-align:center;line-height:10px;padding-top:11px}
.offer .meta{position:absolute;left:10px;right:10px;top:121px;font-size:6.5px;color:var(--muted)}
.offer .meta .r{position:absolute;right:0;top:0;text-align:right;color:#444}
.offer h3{font-family:"Ubuntu",sans-serif;font-weight:400;font-size:10.5px;color:var(--navy);margin:2px 0 2px}
.offer .price{font-family:"Ubuntu",sans-serif;font-weight:500;color:var(--sky);font-size:10.5px;display:block;margin:2px 0}
.offer .start b{font-weight:600;color:#555}

/* footer */
.site-footer{left:0;top:871px;width:686px;height:262px;background:var(--navy)}
.fcol{top:42px;color:#dfe3ea}
.fcol h4{font-family:"Ubuntu",sans-serif;font-weight:400;font-size:13px;color:var(--white);margin-bottom:11px}
.fcol li{font-size:6.6px;line-height:11.8px;padding-left:6px;position:relative}
.fcol li::before{content:"";position:absolute;left:0;top:4.5px;width:2px;height:2px;border-top:1px solid var(--red);border-right:1px solid var(--red);transform:rotate(45deg)}
.contact-row{position:relative;padding-left:16px;font-size:6.6px;line-height:10.5px;margin-bottom:11px}
.contact-row svg{position:absolute;left:0;top:1px}
.about p{font-size:6.6px;line-height:10.8px;width:145px;margin-bottom:22px}
.social-names{display:flex;gap:9px;font-size:7px;margin-top:26px;color:var(--white)}
.legal-bar{left:0;top:1133px;width:686px;height:67px;background:var(--navy-deep);color:#cfd4dc;font-size:6.3px}
.legal-bar nav{position:absolute;top:20px;display:flex;gap:13px}
.partner{position:absolute;background:#3a4560}
</style>
</head>
<body>

<header class="site-header abs">
  <div class="brand abs">Velmora Journeys</div>
  <nav class="main-nav abs">
    <span class="active">Home</span><span>Fjords</span><span>Capitals</span><span>Cruises</span><span>Winter</span><span>Pictures</span><span>Contact</span>
  </nav>
  <div class="lang abs"><b>EN</b><i>|</i>DE</div>
</header>

<section class="hero abs" role="img" aria-label="Aerial photograph of a deep blue fjord with steep green cliffs, a waterfall and a small ferry">
  <form class="search-panel abs">
    <div class="field select">All Destinations</div>
    <div class="field select">All Tour Types</div>
    <div class="field select">All Tour Selections</div>
    <div class="field select">All Travel Periods</div>
    <div class="field text">Free Search
      <svg width="11" height="11" viewBox="0 0 11 11"><circle cx="4.5" cy="4.5" r="3.5" fill="none" stroke="#ccc" stroke-width="1.2"/><path d="M7 7l3 3" stroke="#ccc" stroke-width="1.2"/></svg>
    </div>
    <div class="search-btn">SEARCH</div>
  </form>
  <div class="hero-copy abs">
    <h1>Spectacular Fjords</h1>
    <p>Included on the Global Heritage Council list and Wanderlust Atlas Magazine has ranked them the most popular of all World Heritage sites.</p>
    <span class="read-more">Read more</span>
  </div>
  <div class="dots abs"><span></span><span></span><span></span></div>
</section>

<svg class="abs slider-arrow" style="left:8px" width="10" height="18" viewBox="0 0 10 18"><path d="M9 1L1 9l8 8" fill="none" stroke="#ccc" stroke-width="1.5"/></svg>
<svg class="abs slider-arrow" style="left:668px" width="10" height="18" viewBox="0 0 10 18"><path d="M1 1l8 8-8 8" fill="none" stroke="#ccc" stroke-width="1.5"/></svg>

<a class="tile abs" style="left:30px;background:linear-gradient(180deg,#3b4666,#7a5a40 60%,#b8803a)" role="img" aria-label="Colourful harbour houses of a Norwegian town at dusk"><span class="label">Norway Tours</span></a>
<a class="tile abs" style="left:190px;background:linear-gradient(180deg,#8aa0be,#c98a52 55%,#44628a)" role="img" aria-label="Stockholm old town rooftops by the water"><span class="label">Sweden Tours</span></a>
<a class="tile abs" style="left:351px;background:linear-gradient(180deg,#7d8c95,#5f7f3c 55%,#8aa04a)" role="img" aria-label="Tall waterfall over green Icelandic cliffs"><span class="label">Iceland Tours</span></a>
<a class="tile abs" style="left:512px;background:linear-gradient(180deg,#6e7468,#8f8a74 55%,#b2b0a4)" role="img" aria-label="Cyclists on a gravel road beside a river"><span class="label">Combination Tours</span></a>

<section class="features abs">
  <div class="feature abs" style="left:30px;top:23px">
    <span class="ico"><svg width="27" height="27"><path d="M12 9l5 4.5-5 4.5" fill="none" stroke="#fff" stroke-width="2"/></svg></span>
    <div class="txt"><small>Scandinavian</small><strong>Specialist</strong>
      <p>We are specialist in package tours to Scandinavia. Independent and escorted tours including the Capitals, Fjords, cruises. <b>Book your Scandinavia holiday online!</b></p></div>
  </div>
  <div class="feature abs" style="left:190px;top:23px">
    <span class="ico"><svg width="27" height="27"><path d="M12 9l5 4.5-5 4.5" fill="none" stroke="#fff" stroke-width="2"/></svg></span>
    <div class="txt"><small>Travel</small><strong>Experience</strong></div>
  </div>
  <div class="feature abs" style="left:351px;top:23px">
    <span class="ico"><svg width="27" height="27"><path d="M12 9l5 4.5-5 4.5" fill="none" stroke="#fff" stroke-width="2"/></svg></span>
    <div class="txt"><small>Customer</small><strong>Service <em>(FAQ)</em></strong></div>
  </div>
  <div class="feature abs" style="left:512px;top:23px">
    <span class="ico red"><svg width="27" height="27" viewBox="0 0 27 27"><path d="M10 8c-1 1-1.5 2 0 5s4 5.5 6 6c1 .3 2-.5 2.5-1.3l-2-2-1.3.8c-1-.5-2.5-2-3-3l.8-1.3-2-2z" fill="#fff"/></svg></span>
    <div class="txt"><small>Contact</small><strong>Information</strong></div>
  </div>
  <div class="feature abs" style="left:190px;top:82px">
    <span class="ico"><svg width="27" height="27"><path d="M12 9l5 4.5-5 4.5" fill="none" stroke="#fff" stroke-width="2"/></svg></span>
    <div class="txt"><small>Travel</small><strong>Insurance</strong></div>
  </div>
  <div class="feature abs" style="left:351px;top:82px">
    <span class="ico"><svg width="27" height="27"><path d="M12 9l5 4.5-5 4.5" fill="none" stroke="#fff" stroke-width="2"/></svg></span>
    <div class="txt"><small>Customer</small><strong>Protection</strong></div>
  </div>
  <div class="feature abs" style="left:512px;top:82px">
    <span class="ico social"></span>
    <div class="txt"><small>Like Us On</small><strong class="social-name">Friendwall</strong></div>
  </div>
</section>

<div class="tabs abs"><span class="on">Special Offers</span><span>Populars Tours</span></div>

<svg class="abs" style="left:8px;top:725px" width="10" height="18" viewBox="0 0 10 18"><path d="M9 1L1 9l8 8" fill="none" stroke="#ccc" stroke-width="1.5"/></svg>
<svg class="abs" style="left:668px;top:725px" width="10" height="18" viewBox="0 0 10 18"><path d="M1 1l8 8-8 8" fill="none" stroke="#ccc" stroke-width="1.5"/></svg>

<article class="offer abs" style="left:30px">
  <div class="photo" role="img" aria-label="Husky sled team running across snow" style="background:linear-gradient(180deg,#aab4c4,#e6ebf1 60%,#f6f7fa)"></div>
  <div class="badge">10%<br>OFF</div>
  <div class="meta">Finland Winter Tours<h3>Lapland Winter Adventure</h3><span class="start">Start in <b>Kittilä</b></span>
    <div class="r">6 days<span class="price">€ 599</span>Jan - Apr</div></div>
</article>
<article class="offer abs" style="left:244px">
  <div class="photo" role="img" aria-label="Red brick castle with towers beside a lake" style="background:linear-gradient(180deg,#c9d8e6,#a04a3a 55%,#5a7a3c)"></div>
  <div class="badge">10%<br>OFF</div>
  <div class="meta">Self Drive Tours<h3>Southern Sweden</h3><span class="start">Start in <b>Stockholm</b></span>
    <div class="r">9 days<span class="price">€ 599</span>May - Sep</div></div>
</article>
<article class="offer abs" style="left:458px">
  <div class="photo" role="img" aria-label="Green fjord hillside with farmhouses above turquoise water" style="background:linear-gradient(180deg,#4d6a3a,#6f9a42 60%,#4aa3a3)"></div>
  <div class="badge">10%<br>OFF</div>
  <div class="meta">Independent Short Breaks<h3>Oslo &amp; Sognefjord Exp.</h3><span class="start">Start in <b>Oslo</b></span>
    <div class="r">4 days<span class="price">€ 579</span>May - Sep</div></div>
</article>

<footer class="site-footer abs">
  <div class="fcol abs" style="left:30px">
    <h4>Tour Selections</h4>
    <ul><li>Fjord Tours</li><li>Scandinavian Capitals</li><li>Scandinavia Cruise Packages</li><li>Exclusive Tours</li><li>Midnight Sun</li><li>Activity Tours</li><li>Meet the Locals</li><li>Northern Lights</li><li>Norway Tours</li><li>Sweden Tours</li><li>Iceland Tours</li><li>Göta Canal Cruises</li><li>Coastal Express Cruises</li></ul>
  </div>
  <div class="fcol abs" style="left:190px">
    <h4>Tour Types</h4>
    <ul><li>Escorted Coach Tours</li><li>Independent Rail Tours</li><li>Winter Tours</li><li>Independent Short Breaks)</li><li>Partly Escorted Tours</li><li>Scandinavian Cruises</li><li>Self Drive Tours</li><li>Arctic River Igloo Hotel</li><li>Northern Lights Cruise</li><li>Lapland Winter Adventure</li><li>Baltic &amp; Russian Explorer</li><li>Iceland Wilderness</li><li>Baltic Classical</li></ul>
  </div>
  <div class="fcol abs" style="left:351px">
    <h4>Contact Information</h4>
    <div class="contact-row"><svg width="8" height="10" viewBox="0 0 8 10"><path d="M4 0a4 4 0 014 4c0 3-4 6-4 6S0 7 0 4a4 4 0 014-4z" fill="#c0161c"/><circle cx="4" cy="4" r="1.5" fill="#1f2a3f"/></svg>Fjellgata 14, N-0571 Oslo,<br>Norway</div>
    <div class="contact-row"><svg width="9" height="9" viewBox="0 0 9 9"><path d="M1.5 0.5c-1 1-1 2 .5 4s3 3.5 4.5 4c.8.2 1.5-.3 2-1L7 6l-1 .6C5 6 3.3 4.3 3 3.5l.6-1L2 .5z" fill="#c0161c"/></svg>+47 21 55 08 40 &nbsp;| &nbsp;NO 915 340 618</div>
    <div class="contact-row"><svg width="10" height="9" viewBox="0 0 10 9"><rect x="2" y="0" width="6" height="3" fill="#c0161c"/><rect x="0" y="3" width="10" height="4" rx="1" fill="#c0161c"/><rect x="2" y="6" width="6" height="3" fill="#c0161c"/></svg>+47 21 55 08 41</div>
    <div class="contact-row"><svg width="10" height="8" viewBox="0 0 10 8"><rect width="10" height="8" fill="#c0161c"/><path d="M0 0l5 4 5-4" fill="none" stroke="#1f2a3f"/></svg>info@velmora-journeys.com</div>
    <div class="social-names"><span>Friendwall</span><span>Feed</span><span>Chirper</span><span>Circles</span><span>Snapgram</span></div>
  </div>
  <div class="fcol abs about" style="left:512px">
    <h4>Velmora Journeys</h4>
    <p>Specialist in package tours to Scandinavia. Velmora Journeys is a dedicated online tour operator, creating and selling independent package tours and escorted coach tours throughout Scandinavia.</p>
    <ul><li>About Us</li><li>Booking &amp; Payment</li><li>Terms &amp; Conditions</li></ul>
  </div>
</footer>

<div class="legal-bar abs">
  <nav style="left:30px"><span>Home</span><span>Fjords</span><span>Capitals</span><span>Cruises</span><span>Winter</span><span>Pictures</span><span>Contact</span></nav>
  <nav style="right:29px"><span>FAQ's</span><span>Photo Credits</span><span>Book Rental Car</span><span>Site Map</span></nav>
  <div class="abs" style="left:30px;top:44px">© 2015 Velmora Journeys A.S. All rights reserved.</div>
  <span class="partner" style="left:315px;top:27px;width:50px;height:17px;border-radius:2px"></span>
  <span class="partner" style="left:389px;top:16px;width:42px;height:42px;border-radius:50%"></span>
  <span class="partner" style="left:530px;top:39px;width:22px;height:12px;border-radius:2px"></span>
  <span class="partner" style="left:562px;top:39px;width:22px;height:12px;border-radius:2px"></span>
  <span class="partner" style="left:596px;top:39px;width:22px;height:12px;border-radius:2px"></span>
  <span class="partner" style="left:628px;top:39px;width:28px;height:12px;border-radius:2px"></span>
</div>

</body>
</html>
```